Plakat-Design für Anbieter von qualitativen und nachhaltigen Menstruationsprodukten
Zielgruppe
Wir bieten qualitative und nachhaltige Menstruationsprodukte aus zertifizierter Bio-Baumwolle, die du dir bequem im personalisierten Abo nach Hause liefern lassen kannst. Mit jeder gekauften Box unterstützt du ausserdem ein soziales Projekt. Auf unserer Website kann die Abo- Box individuell zusammengestellt und im gewünschten Zyklus bestellt werden.
Unsere Zielgruppe sind menstruierende Personen im Alter zwischen 18 und 34 mit dem Bedarf an nachhaltigen Produkten ohne schädliche Inhaltsstoffe und dem Wunsch soziale Projekte zu unterstützen.
Aufgabenstellung
Wir dürfen an einem Openair beim Kiosk gratis Menstruationsprodukte herausgeben. Das Plakat wird beim Kiosk platziert, damit die Personen darüber informiert sind.
Wir benötigen noch Hilfe bei der Message des Plakates.
Die Message sollte einerseits die Information darüber beinhalten wie z.B.: Gratis Periodenprodukte beim Kiosk
Anderseits sollte unsere Firma im Plakat repräsentiert sein. Wie z.B. Du hast keine Periodenprodukte dabei? Dank Welvana musst du nicht mehr daran denken....

```html
<!DOCTYPE html>
<html lang="de">
<head>
<meta charset="utf-8">
<title>Welvana – Gratis hier im Kiosk</title>
<link href="https://fonts.googleapis.com/css2?family=Raleway:ital,wght@0,500;0,600;0,800;1,700&family=Montserrat:wght@400;700&display=swap" rel="stylesheet">
<style>
  :root {
    --page-bg: #eceaeb;
    --plum: #8b6a84;
    --plum-light: #9a7893;
    --plum-text: #7c5775;
    --band: #f5f0f3;
    --white: #ffffff;
    --photo-a: #d7b2a8;
    --photo-b: #c89f95;
    --photo-c: #e6cfc7;
    --sticker: #d6b48c;
  }
  * { margin: 0; padding: 0; box-sizing: border-box; }
  html, body { width: 1120px; height: 1200px; overflow: hidden; background: var(--page-bg); }
  .poster {
    position: absolute; left: 140px; top: 0; width: 840px; height: 1200px;
    overflow: hidden; font-family: "Montserrat", sans-serif;
  }
  .hero-photo {
    position: absolute; left: 0; top: 0; width: 840px; height: 681px;
    background:
      radial-gradient(ellipse at 55% 60%, var(--photo-c) 0%, transparent 55%),
      linear-gradient(135deg, #7f8a6e 0%, var(--photo-b) 30%, var(--photo-a) 60%, var(--photo-c) 100%);
  }
  .site-url {
    position: absolute; right: 70px; top: 58px;
    font-family: "Raleway", sans-serif; font-weight: 600; font-size: 20px; color: var(--white);
  }
  .brand-seal {
    position: absolute; left: 320px; top: 65px; width: 194px; height: 194px;
    border-radius: 50%; background: var(--white);
    display: flex; align-items: center; justify-content: center;
  }
  .brand-name {
    font-family: "Raleway", sans-serif; font-weight: 500; font-size: 28px;
    letter-spacing: 3px; color: var(--plum-text);
  }
  .values-sticker {
    position: absolute; left: 650px; top: 492px; width: 126px; height: 126px;
    border-radius: 50%; background: var(--sticker);
  }
  .question-band {
    position: absolute; left: 0; top: 681px; width: 840px; height: 86px;
    background: var(--band); display: flex; align-items: center; padding-left: 66px;
  }
  .question {
    font-family: "Raleway", sans-serif; font-weight: 600; font-size: 36px; color: var(--plum-text);
  }
  .offer-panel {
    position: absolute; left: 0; top: 767px; width: 840px; height: 433px;
    background: linear-gradient(180deg, var(--plum) 0%, var(--plum-light) 100%);
    color: var(--white);
  }
  .offer-lead {
    position: absolute; left: 66px; top: 50px;
    font-family: "Raleway", sans-serif; font-weight: 500; font-size: 38px;
  }
  .offer-main {
    position: absolute; left: 64px; top: 100px;
    font-family: "Raleway", sans-serif; font-weight: 800; font-size: 75px; letter-spacing: -0.5px;
  }
  .column-title {
    position: absolute; top: 218px;
    font-family: "Raleway", sans-serif; font-weight: 700; font-style: italic; font-size: 21px;
  }
  .about {
    position: absolute; left: 66px; top: 276px; font-size: 13px; line-height: 20.5px;
    white-space: nowrap;
  }
  .about strong { font-weight: 700; }
  .about p { font-weight: 400; opacity: 0.92; }
  .benefits { position: absolute; left: 545px; top: 276px; list-style: none; font-size: 13px; line-height: 20.5px; }
  .benefits li { display: flex; align-items: center; gap: 9px; opacity: 0.92; }
  .benefits svg { width: 10px; height: 10px; }
</style>
</head>
<body>
  <div class="poster">
    <div class="hero-photo" role="img" aria-label="Hand öffnet eine Kartonbox mit weiss verpacktem Päckchen, Schnur und Lavendel auf rosa Tüll mit Palmblatt und Eukalyptus"></div>
    <div class="site-url">www.welvana.ch</div>
    <div class="brand-seal"><span class="brand-name">WELVANA</span></div>
    <div class="values-sticker" role="img" aria-label="Runder Werte-Sticker der Marke"></div>
    <div class="question-band">
      <h2 class="question">Du hast keine Periodenprodukte dabei?</h2>
    </div>
    <section class="offer-panel">
      <p class="offer-lead">Dann schnapp dir deine Probe</p>
      <h1 class="offer-main">Gratis hier im Kiosk!</h1>
      <h3 class="column-title" style="left:66px">Welvana - for every body</h3>
      <h3 class="column-title" style="left:545px">So fresh &amp; clean</h3>
      <div class="about">
        <strong>Individuell zusammengestellt – nach deinem Zyklus geliefert.</strong>
        <p>Qualitative und nachhaltige Menstruationsprodukte aus zertifizierter<br>Bio-Baumwolle, die du dir bequem im personalisierten Abo nach<br>Hause liefern lassen kannst. Mit jeder gekauften Box unterstützt<br>du ausserdem ein soziales Projekt.</p>
      </div>
      <ul class="benefits">
        <li><svg viewBox="0 0 10 10"><path d="M1 5.5 L4 8.5 L9 1.5" fill="none" stroke="currentColor" stroke-width="1.4"/></svg>aus zertifizierter Bio-Baumwolle</li>
        <li><svg viewBox="0 0 10 10"><path d="M1 5.5 L4 8.5 L9 1.5" fill="none" stroke="currentColor" stroke-width="1.4"/></svg>hypoallergen</li>
        <li><svg viewBox="0 0 10 10"><path d="M1 5.5 L4 8.5 L9 1.5" fill="none" stroke="currentColor" stroke-width="1.4"/></svg>vegan &amp; tierversuchsfrei</li>
        <li><svg viewBox="0 0 10 10"><path d="M1 5.5 L4 8.5 L9 1.5" fill="none" stroke="currentColor" stroke-width="1.4"/></svg>frei von Plastik</li>
        <li><svg viewBox="0 0 10 10"><path d="M1 5.5 L4 8.5 L9 1.5" fill="none" stroke="currentColor" stroke-width="1.4"/></svg>ohne Parfüm und Superabsorber</li>
      </ul>
    </section>
  </div>
</body>
</html>
```